Motivational Quotes Poster Series

This is a 3 poster design series for Ridgeway Haul Academy. The size of each poster should be 18 inches wide and 24 inches tall. The goal of these posters is to serve as motivational "signs" to be hung in the office area for the employees (not customers). These employees are instructors/teachers, teaching students how to drive semi trucks. While each design is a separate poster and design, we're posting as 1 project because we'd like some continuity between the series. Below we'll break down the details of all 3 posters...

Poster #1
Text that must appear on poster - "If You Want The Best Out Of Each Student" and "Give The Best Of You!" Note: While this text must appear on the poster, you can arrange in the layout as you see fit. For example, first line could be at top of poster and second line on bottom.

Poster #2
Text that must appear on poster - "Invest In People" and "Change Someone's Life" (same notes apply as in 1st poster)

Poster #3
Text that must appear on poster - "Today Is..." and "Just Another Day For You" and "The Most Important Day In Their Life" Note: This can be laid out on the poster however you see fit, but each phrase needs to be separate and it needs to flow.

Target Market(s)

Truck Driver Training Instructors - These are middle-aged, mostly male, masculine type personalities.

Industry/Entity Type

Training

Requirements
Must have
• Must have noted text from description
Must have working files (ie - PSD, EPS, AI, etc) provided
Must have common theme between each poster in series
Must have easy to read font and layout
Must have product dimensions of 18 inches (width) by 24 inches (height). If design uses full dimensions please include quarter inch bleed.
Nice to have
• Nice to have a trucking theme...related to trucking industry, but not over the top. Example - This could mean subtle injection of background tire tracks, but by no means are tire tracks required.

For inspiration, you can visit the site at http://www.ridgewayhaulacademy.com. While you can use the colors of the site/logo, you can still branch out between each poster to try new colors within reason.

Note: While we've attached the logo to this project, it COULD be used but doesn't HAVE to be included in the design. The logo IS NOT a focal point. The phrases in the poster ARE the focal point.

```html
<!DOCTYPE html>
<html lang="en">
<head>
<meta charset="utf-8">
<title>Today Is… — Ridgeway Haul Academy Poster</title>
<link rel="stylesheet" href="https://fonts.googleapis.com/css2?family=Bebas+Neue&display=swap">
<style>
  :root {
    --page: #ffffff;
    --field: #2eaa6a;
    --track-band: #279a5e;
    --headline: #0b4527;
    --calendar-line: #000000;
    --marker: #b3322a;
  }
  html, body {
    margin: 0;
    padding: 0;
    width: 900px;
    height: 1200px;
    overflow: hidden;
    background: var(--page);
  }
  .poster {
    display: block;
    width: 900px;
    height: 1200px;
  }
  .poster text {
    font-family: "Bebas Neue", "Oswald", sans-serif;
  }
  .field { fill: var(--field); }
  .tire-track { fill: var(--track-band); }
  .calendar-rule {
    stroke: var(--calendar-line);
    stroke-width: 6;
    fill: none;
  }
  .calendar-label {
    fill: var(--calendar-line);
    font-size: 92px;
  }
  .today-marker {
    fill: none;
    stroke: var(--marker);
    stroke-width: 16;
    stroke-linecap: round;
    opacity: 0.6;
  }
  .headline {
    fill: var(--headline);
    font-size: 142px;
    opacity: 0.92;
  }
  .academy-name {
    fill: var(--calendar-line);
    font-size: 22px;
  }
  .academy-dot { fill: var(--calendar-line); }
</style>
</head>
<body>
<svg class="poster" viewBox="0 0 900 1200" xmlns="http://www.w3.org/2000/svg">
  <defs>
    <clipPath id="field-clip">
      <rect x="27" y="33" width="846" height="1134"/>
    </clipPath>
  </defs>

  <rect class="field" x="27" y="33" width="846" height="1134"/>

  <g clip-path="url(#field-clip)">
    <rect class="tire-track" x="30" y="33" width="182" height="1134" role="img" aria-label="Faint tire tread tracks running down the poster"/>
    <rect class="tire-track" x="688" y="33" width="182" height="1134" role="img" aria-label="Faint tire tread tracks running down the poster"/>

    <g class="calendar">
      <line class="calendar-rule" x1="0" y1="347" x2="900" y2="347"/>
      <line class="calendar-rule" x1="0" y1="507" x2="900" y2="507"/>
      <line class="calendar-rule" x1="0" y1="852" x2="900" y2="852"/>
      <line class="calendar-rule" x1="189" y1="347" x2="189" y2="852"/>
      <line class="calendar-rule" x1="200" y1="347" x2="200" y2="852"/>
      <line class="calendar-rule" x1="700" y1="347" x2="700" y2="852"/>
      <line class="calendar-rule" x1="712" y1="347" x2="712" y2="852"/>
      <text class="calendar-label" x="183" y="460" text-anchor="end">YESTERDAY</text>
      <text class="calendar-label" x="450" y="460" text-anchor="middle">TODAY</text>
      <text class="calendar-label" x="772" y="460">TOMORROW</text>
    </g>

    <path class="today-marker" d="M232 378 C 330 330, 560 340, 640 420 C 720 500, 700 660, 600 750 C 500 830, 320 800, 250 700 C 190 610, 200 470, 300 380"/>

    <g class="headline-group">
      <text class="headline" x="450" y="150" text-anchor="middle" textLength="462" lengthAdjust="spacingAndGlyphs">TODAY IS...</text>
      <text class="headline" x="450" y="390" text-anchor="middle" textLength="818" lengthAdjust="spacingAndGlyphs">JUST ANOTHER DAY</text>
      <text class="headline" x="450" y="562" text-anchor="middle" textLength="356" lengthAdjust="spacingAndGlyphs">FOR YOU</text>
      <text class="headline" x="450" y="803" text-anchor="middle" textLength="424" lengthAdjust="spacingAndGlyphs">THE MOST</text>
      <text class="headline" x="450" y="980" text-anchor="middle" textLength="686" lengthAdjust="spacingAndGlyphs">IMPORTANT DAY</text>
      <text class="headline" x="450" y="1150" text-anchor="middle" textLength="560" lengthAdjust="spacingAndGlyphs">IN THEIR LIFE</text>
    </g>

    <g class="academy-mark">
      <rect class="academy-dot" x="36" y="1128" width="18" height="18"/>
      <text class="academy-name" x="60" y="1146">Ridgeway Haul Academy</text>
    </g>
  </g>
</svg>
</body>
</html>
```